Bathroom Remodeling Guide Needed

We need to create a Bathroom remodeling guide that we can give away as a freemium download. The attached file contains the instructions and copy for the guide along with our logo. Below is a dropbox link to our assets folder as well.

https://www.filevantor.com/shr/fd/q7kzmwtrpl4bxe829hcvua/KTRmWqvbPzXc3hLyJuGaTo5?rkey=7hvbq2093kw8tf1ma5512d48x&dl=0

```html
<!DOCTYPE html>
<html lang="en">
<head>
<meta charset="utf-8">
<title>Hearthline Kitchen &amp; Bath — Bathroom Remodeling Guide</title>
<link rel="stylesheet" href="https://fonts.googleapis.com/css2?family=Cinzel:wght@400;500&family=Marcellus&family=Jost:wght@400;500;600&display=swap">
<style>
:root{
  --navy:#14304f;
  --ink:#1c2430;
  --paper:#ffffff;
  --stage:#f1f1f1;
  --rule:#8a97a8;
  --sand:#d9cbb8;
  --sky:#b9d3e0;
}
*{box-sizing:border-box;margin:0;padding:0}
html,body{width:791px;height:1200px;overflow:hidden;background:var(--stage)}
body{font-family:"Jost",sans-serif;color:var(--ink)}
.spread{position:relative;width:791px;height:1200px}
.page{position:absolute;width:234px;height:303px;background:var(--paper);overflow:hidden;box-shadow:0 1px 4px rgba(0,0,0,.12)}
.p1{left:24px;top:284px}.p2{left:278px;top:284px}.p3{left:532px;top:284px}
.p4{left:24px;top:611px}.p5{left:278px;top:611px}.p6{left:532px;top:611px}
.photo{position:absolute}
.frame{position:absolute;left:12px;top:12px;right:12px;bottom:-4px;border:2px solid var(--navy);border-bottom:none}
.brand{position:absolute;left:0;right:0;text-align:center;font-family:"Jost",sans-serif;font-weight:500;color:var(--navy);letter-spacing:.06em}
.brand span{display:inline-block;width:5px;height:5px;background:var(--navy);margin-right:4px;vertical-align:middle}
.center{position:absolute;left:0;right:0;text-align:center}
.display{font-family:"Cinzel",serif;color:var(--navy);line-height:.98}
.head{font-family:"Marcellus",serif;color:var(--navy);line-height:1.1}
.body{font-size:3.6px;line-height:1.45;color:var(--ink)}
.body p{margin-bottom:3px}
.body ul{list-style:none}
.body li::before{content:"• "}
.footer-rule{position:absolute;height:6px}
.on-navy{color:#e8eef5}
.on-navy .head{color:#ffffff}
</style>
</head>
<body>
<main class="spread">

  <!-- Cover -->
  <section class="page p1">
    <div class="photo" role="img" aria-label="Bright white bathroom with freestanding tub before tall windows looking out to the sea and palm trees" style="left:0;top:170px;width:234px;height:133px;background:linear-gradient(180deg,#fff 0%,#dfeaf0 30%,#a9c7d6 60%,#e6e3de 100%)"></div>
    <div class="frame"></div>
    <div class="brand" style="top:30px;font-size:11px">HEARTHLINE<div style="font-size:4.5px;letter-spacing:.25em;margin-top:1px">KITCHEN &amp; BATH</div></div>
    <div class="center" style="top:70px;font-size:7.5px">The Homeowner’s Guide to</div>
    <div class="center display" style="top:82px;font-size:20px">BATHROOM<br>REMODELING<br>IN CHARLOTTE</div>
    <div style="position:absolute;left:28px;right:28px;top:144px;height:1px;background:var(--navy)"></div>
    <div class="center" style="top:147px;font-size:4.6px">How to Plan, Design, and Build a Bathroom You’ll Love for Years to Come</div>
    <div class="center head" style="top:158px;font-size:8.5px">HEARTHLINE KITCHEN &amp; BATH</div>
  </section>

  <!-- Before you start -->
  <section class="page p2 on-navy" style="background:var(--navy)">
    <div class="photo" role="img" aria-label="Bathroom with wooden slat wall, freestanding tub and green plants" style="left:15px;top:25px;width:205px;height:83px;background:linear-gradient(120deg,#e9e3da,#b98a52 50%,#dcd7cf)"></div>
    <div class="photo" role="img" aria-label="Small bathroom with round mirror and red rug" style="left:15px;top:112px;width:73px;height:73px;background:linear-gradient(180deg,#f4efe8,#e6c9a0 70%,#c8452e)"></div>
    <div class="photo" role="img" aria-label="Wood vanity beside glass shower enclosure" style="left:92px;top:112px;width:128px;height:73px;background:linear-gradient(110deg,#b88c5e,#d9d6d2 55%,#eef0f1)"></div>
    <div class="head" style="position:absolute;left:15px;top:192px;font-size:11.5px">Before You Start Your<br>Bathroom Remodel</div>
    <div class="body" style="position:absolute;left:15px;right:14px;top:223px;color:#d9e2ec">
      <p>Remodeling your bathroom is one of the most impactful upgrades you can make to your home. Done right, it improves how you start and end your day, increases your home’s value, and creates a space that feels both functional and refined.</p>
      <p>But without the right plan, it can quickly become overwhelming.</p>
      <p>Many homeowners begin with inspiration photos and good intentions, only to run into unexpected costs, delays, and decisions they weren’t prepared for.</p>
      <p>This guide was created to give you clarity before you begin—so you can move forward with confidence, avoid common mistakes, and ultimately achieve a result you’ll be proud of for years to come.</p>
    </div>
    <svg class="footer-rule" style="left:15px;top:288px;width:206px" viewBox="0 0 206 6"><line x1="0" y1="3" x2="200" y2="3" stroke="#c9d3de" stroke-width=".6"/><circle cx="202.5" cy="3" r="2.2" fill="none" stroke="#c9d3de" stroke-width=".6"/></svg>
  </section>

  <!-- Most remodels go wrong -->
  <section class="page p3">
    <div class="head" style="position:absolute;left:15px;top:15px;font-size:9.5px">Most Bathroom Remodels Go<br>Wrong Before They Even Start</div>
    <div class="body" style="position:absolute;left:15px;right:14px;top:41px">
      <p>The success of a bathroom remodel is determined long before construction begins.</p>
      <p>The most common mistake homeowners make is starting without a clear, well-thought-out plan. Decisions are made on the fly, materials are selected too late, and small issues quickly turn into costly problems.</p>
    </div>
    <div class="head" style="position:absolute;left:15px;top:64px;font-size:6.2px">A Successful Project Requires:</div>
    <div class="body" style="position:absolute;left:17px;right:14px;top:73px">
      <ul><li>A clear design vision</li><li>Thoughtful material selection</li><li>Proper planning before demolition</li><li>A team that understands both design and construction</li></ul>
      <p style="margin-top:3px">When these elements are in place, the process becomes smooth, predictable, and even enjoyable.</p>
      <p>When they’re not, the experience is often the opposite.</p>
    </div>
    <div class="photo" role="img" aria-label="Warm neutral bathroom with arched niche, freestanding tub and gold-framed mirror" style="left:0;top:124px;width:234px;height:154px;background:linear-gradient(110deg,#f3efe9,#e3d7c6 45%,#cdb89c 80%,#e9e1d5)"></div>
    <svg class="footer-rule" style="left:15px;top:285px;width:206px" viewBox="0 0 206 6"><line x1="0" y1="3" x2="200" y2="3" stroke="var(--rule)" stroke-width=".6"/><circle cx="202.5" cy="3" r="2.2" fill="none" stroke="var(--rule)" stroke-width=".6"/></svg>
  </section>

  <!-- Costs -->
  <section class="page p4">
    <div class="photo" role="img" aria-label="White marble bathroom with black-framed glass shower and black vanity" style="left:0;top:0;width:234px;height:182px;background:linear-gradient(100deg,#2a2a2a 0%,#e8e8e6 25%,#f5f4f2 55%,#262626 75%,#d8d4ce)"></div>
    <div class="display" style="position:absolute;left:15px;top:193px;font-size:8.4px;line-height:1.1">UNDERSTANDING<br>BATHROOM<br>REMODELING COSTS</div>
    <div class="body" style="position:absolute;left:15px;width:96px;top:225px">
      <p style="text-align:justify">Every bathroom remodel is unique, but most projects fall within a predictable range depending on size, scope, and finishes.</p>
      <p>At Hearthline Kitchen &amp; Bath, most bathroom remodeling</p>
    </div>
    <div class="head" style="position:absolute;left:15px;top:252px;font-size:8px">Projects Start at $35,000</div>
    <div class="body" style="position:absolute;left:15px;width:96px;top:262px"><p>and increase based on complexity, materials, and customization.</p></div>
    <div class="head" style="position:absolute;left:130px;top:193px;font-size:5.6px">Several factors influence the<br>total investment:</div>
    <div class="body" style="position:absolute;left:130px;width:92px;top:207px">
      <ul><li>The size of the space</li><li>Tile selection and layout complexity</li><li>Plumbing or layout changes</li><li>Custom vanities and cabinetry</li><li>Lighting and fixture upgrades</li><li>Specialty features such as walk-in showers or freestanding tubs</li></ul>
      <p style="margin-top:3px;text-align:justify">Rather than focusing on the lowest possible cost, our approach is to deliver long-term value—combining thoughtful design, quality materials, and expert craftsmanship.</p>
    </div>
    <svg class="footer-rule" style="left:15px;top:285px;width:206px" viewBox="0 0 206 6"><line x1="0" y1="3" x2="200" y2="3" stroke="var(--rule)" stroke-width=".6"/><circle cx="202.5" cy="3" r="2.2" fill="none" stroke="var(--rule)" stroke-width=".6"/></svg>
  </section>

  <!-- Design foundation -->
  <section class="page p5">
    <div class="head" style="position:absolute;left:13px;top:15px;font-size:11px;line-height:1.05">Why Design Is<br>the Foundation<br>of a Successful<br>Remodel</div>
    <div class="body" style="position:absolute;left:13px;width:92px;top:65px"><p>A beautiful bathroom doesn’t happen by accident—it is designed.</p></div>
    <div class="body" style="position:absolute;left:118px;width:103px;top:14px">
      <p>Layout, lighting, storage, and material selection must all work together to create a space that feels cohesive and functions effortlessly.</p>
      <p>Every project we take on includes a professional designer at no additional cost. This ensures that your bathroom is carefully planned before construction begins, eliminating guesswork and reducing the likelihood of costly changes later.</p>
      <p>With a clear design in place, you’ll be able to visualize your new space, make confident decisions, and move into construction with clarity.</p>
    </div>
    <div class="photo" role="img" aria-label="Bathroom sketch turning into a finished room, framed between two hands" style="left:0;top:82px;width:234px;height:108px;background:linear-gradient(90deg,#f6f6f4,#ece7df 45%,#d9c6a2 75%,#f2efe9)"></div>
    <div class="photo" role="img" aria-label="Grey bathroom with round mirror and wood vanity" style="left:0;top:194px;width:115px;height:80px;background:linear-gradient(120deg,#d6d3ce,#a98a6a 70%,#cfccc6)"></div>
    <div class="photo" role="img" aria-label="White bathroom with freestanding tub and open wood shelving" style="left:119px;top:194px;width:115px;height:80px;background:linear-gradient(120deg,#f3f1ee,#e5ded3 60%,#c9a77d)"></div>
    <svg class="footer-rule" style="left:13px;top:285px;width:208px" viewBox="0 0 208 6"><line x1="0" y1="3" x2="202" y2="3" stroke="var(--rule)" stroke-width=".6"/><circle cx="204.5" cy="3" r="2.2" fill="none" stroke="var(--rule)" stroke-width=".6"/></svg>
  </section>

  <!-- Back cover CTA -->
  <section class="page p6">
    <div class="photo" role="img" aria-label="Spa-like bathroom with freestanding tub, wood vanity and glass shower" style="left:0;top:190px;width:234px;height:113px;background:linear-gradient(180deg,#fff 0%,#ece8e2 30%,#b9a58b 70%,#d7d1c8)"></div>
    <div class="frame"></div>
    <div class="brand" style="top:44px;font-size:11px">HEARTHLINE<div style="font-size:4.5px;letter-spacing:.25em;margin-top:1px">KITCHEN &amp; BATH</div></div>
    <div class="center display" style="top:105px;font-size:14px">LET’S DESIGN<br>YOUR BATHROOM</div>
    <div class="center" style="top:137px;font-size:4.6px">The best place to start is with a conversation.</div>
    <div class="center" style="top:147px;font-size:4.6px;line-height:1.3;padding:0 36px">We’ll help you clarify your vision, explore your options, and create a plan tailored specifically to your home.</div>
    <div class="center" style="top:164px;font-size:7.8px;font-weight:600;color:#111">Schedule Your Design Consultation</div>
    <div class="center" style="top:178px;font-size:4.6px">Hearthline Kitchen &amp; Bath Charlotte, NC</div>
  </section>

</main>
</body>
</html>
```